Escrow Accounting firm needs a website design for a startup that services clients nationally.

I offer escrow accounting services for title companies and real estate attorneys. I've enclosed a logo, color palette and flyers with content that can be used for the site.

I'm looking for a similar design concept as the website below from my former employer. Please don't copy because of copyright infringement. Including for design ideas only.
www.harborlineaccounting.com

Below is a brief write-up...
For professionals in the title insurance industry, finding a trustworthy and budget-friendly solution for escrow accounting can be daunting. When choosing the right accounting partner, title companies and law firms need a group they can rely on, and that's where we come in.

```html
<!DOCTYPE html>
<html lang="en">
<head>
<meta charset="utf-8">
<title>Keystone Ledger Partners — Escrow Accounting</title>
<link rel="stylesheet" href="https://fonts.googleapis.com/css2?family=Playfair+Display:wght@600;700&family=Poppins:wght@400;500;600&display=swap">
<style>
:root{
  --slate:#3b414c;
  --slate-deep:#333842;
  --slate-line:#4a515d;
  --copper:#c27c5e;
  --copper-dark:#ad6a4e;
  --ink:#2f343c;
  --muted:#7b8089;
  --paper:#ffffff;
  --mist:#f3f4f6;
  --border:#e1e3e7;
}
*{box-sizing:border-box;margin:0;padding:0}
html,body{width:1200px;height:2508px;overflow:hidden}
body{font-family:"Poppins",Arial,sans-serif;color:var(--ink);background:var(--paper);font-size:13px;line-height:1.7}
.serif{font-family:"Playfair Display",Georgia,serif}
.wrap{width:1000px;margin:0 auto;position:relative}
.btn{display:inline-block;background:var(--copper);color:#fff;font-size:11px;font-weight:600;letter-spacing:.08em;padding:11px 26px;text-transform:uppercase}
.eyebrow{color:var(--copper);font-size:11px;font-weight:600;letter-spacing:.12em;text-transform:uppercase}

/* top bar */
.topbar{height:32px;background:var(--mist);font-size:11px;color:var(--muted)}
.topbar .wrap{display:flex;justify-content:space-between;align-items:center;height:32px}
.topbar .social{display:flex;gap:8px}
.dot-icon{width:14px;height:14px;border-radius:50%;background:var(--slate)}

/* header */
.site-header{height:80px;background:var(--paper);border-bottom:1px solid var(--border)}
.site-header .wrap{display:flex;align-items:center;height:80px}
.brand{display:flex;align-items:center;gap:10px;font-weight:600;font-size:17px;color:var(--slate);letter-spacing:.03em}
.brand-mark{width:26px;height:26px;background:var(--copper)}
.main-nav{display:flex;gap:30px;margin-left:auto;margin-right:40px;font-size:13px;font-weight:500}
.main-nav a{color:var(--ink);text-decoration:none}
.quote-block{text-align:center}
.quote-block .btn{padding:9px 20px}
.quote-block .phone{font-size:12px;font-weight:600;margin-top:4px;color:var(--slate)}

/* hero */
.hero{height:488px;background:linear-gradient(120deg,var(--slate-deep),var(--slate) 60%,#444b57);color:#fff}
.hero .wrap{height:488px}
.hero-copy{position:absolute;left:0;top:110px;width:560px}
.hero h1{font-size:44px;line-height:1.15;font-weight:700}
.hero .sub{font-size:15px;font-weight:600;letter-spacing:.04em;margin-top:10px;text-transform:uppercase}
.hero p{font-size:12px;color:#c9ccd2;margin-top:12px;width:520px}
.hero .btn{margin-top:28px}
.slider-dots{display:flex;gap:8px;margin-top:34px}
.slider-dots span{width:9px;height:9px;border-radius:50%;background:#7d838d}
.slider-dots span:first-child{background:#fff}
.hero-photo{position:absolute;right:30px;top:78px;width:210px;height:300px;background:linear-gradient(160deg,#e7e2dc,#b9aa9c);border:6px solid #fff}

/* about */
.about{height:440px}
.about .wrap{height:440px}
.about-photo{position:absolute;left:70px;top:60px;width:290px;height:240px;background:linear-gradient(135deg,#dfe6ee,#9fb0c2)}
.years-badge{position:absolute;left:258px;top:188px;width:120px;height:100px;background:#fff;box-shadow:0 6px 20px rgba(0,0,0,.12);text-align:center;padding-top:16px}
.years-badge strong{display:block;font-family:"Playfair Display",Georgia,serif;font-size:34px;line-height:1.1;color:var(--ink)}
.years-badge span{font-size:10px;color:var(--muted)}
.about-copy{position:absolute;left:512px;top:72px;width:440px}
.about-copy h2{font-size:28px;line-height:1.25;margin-top:6px}
.about-copy p{font-size:11.5px;color:var(--muted);margin-top:14px}
.about-copy .btn{margin-top:20px}

/* services */
.services{height:550px;background:var(--slate);color:#fff}
.services .wrap{height:550px;text-align:center}
.services .eyebrow{padding-top:60px;display:block}
.services h2{font-size:30px;line-height:1.25;margin-top:6px}
.service-grid{display:flex;gap:20px;justify-content:center;margin-top:48px;text-align:left}
.service-card{width:254px;height:340px;background:#fff;color:var(--ink);padding:28px 24px;border-radius:4px}
.service-card svg{display:block}
.service-card h3{font-size:18px;line-height:1.25;margin-top:14px}
.service-card p{font-size:11px;color:var(--muted);margin-top:10px}
.service-card .more{display:block;color:var(--copper);font-size:10px;font-weight:600;letter-spacing:.08em;margin-top:14px}

/* contact */
.contact{height:360px}
.contact .wrap{height:360px}
.contact-info{position:absolute;left:0;top:70px;width:390px}
.contact-info h2{font-size:28px;margin-top:4px}
.contact-info p{font-size:11px;color:var(--muted);margin-top:10px}
.contact-list{list-style:none;margin-top:16px;font-size:11px;color:var(--muted)}
.contact-list li{display:flex;align-items:center;gap:10px;margin-bottom:8px}
.contact-form{position:absolute;left:490px;top:70px;width:510px}
.form-row{display:flex;gap:20px;margin-bottom:18px}
.field{flex:1;border-bottom:1px solid var(--border);font-size:11px;color:var(--muted);padding:6px 0}
.field.message{height:64px}
.form-actions{display:flex;align-items:center;gap:18px}
.form-actions .btn{padding:9px 28px}
.consent{display:flex;align-items:center;gap:8px;font-size:10px;color:var(--muted)}
.consent i{width:11px;height:11px;border:1px solid var(--muted);display:block}

/* map */
.map{height:280px;background:linear-gradient(135deg,#e6e9e4,#d3dbd6 55%,#c8d4dc)}

/* footer */
.site-footer{height:230px;background:var(--slate);color:#fff}
.site-footer .wrap{display:flex;padding-top:48px}
.footer-brand{width:460px}
.footer-brand .brand{color:#fff}
.footer-brand p{font-size:11px;color:#b9bdc4;width:250px;margin-top:12px}
.footer-social{display:flex;gap:8px;margin-top:14px}
.footer-social .dot-icon{background:#fff;opacity:.8}
.footer-col{width:210px}
.footer-col h4{font-size:12px;font-weight:600;letter-spacing:.08em;text-transform:uppercase}
.footer-col ul{list-style:none;margin-top:12px;font-size:11px;color:#b9bdc4;line-height:1.9}
.copyright{height:38px;background:var(--copper);color:#fff;font-size:10px;text-align:center;line-height:38px}
</style>
</head>
<body>

<div class="topbar">
  <div class="wrap">
    <span>1210 Harbor View Road, Austin, TX 78701</span>
    <div class="social"><span class="dot-icon"></span><span class="dot-icon"></span><span class="dot-icon"></span></div>
  </div>
</div>

<header class="site-header">
  <div class="wrap">
    <div class="brand"><span class="brand-mark"></span>KEYSTONE LEDGER</div>
    <nav class="main-nav">
      <a href="#">Home</a><a href="#">About Us</a><a href="#">Our Services</a><a href="#">Contact Us</a>
    </nav>
    <div class="quote-block">
      <span class="btn">Request a Quote</span>
      <div class="phone">(555) 018-2044</div>
    </div>
  </div>
</header>

<section class="hero">
  <div class="wrap">
    <div class="hero-copy">
      <h1 class="serif">Trusted Escrow<br>Accounting Solutions</h1>
      <div class="sub">For Title Companies and Real Estate Attorneys</div>
      <p>Navigating the complexities of escrow accounting is easier with a partner you can trust. Our dedicated team reconciles every account with accuracy and care, so title companies and law firms can focus on their clients.</p>
      <span class="btn">Learn More</span>
      <div class="slider-dots"><span></span><span></span><span></span><span></span></div>
    </div>
    <div class="hero-photo" role="img" aria-label="Portrait photo of a smiling escrow accounting professional"></div>
  </div>
</section>

<section class="about">
  <div class="wrap">
    <div class="about-photo" role="img" aria-label="Photo of financial reports and a calculator on a desk"></div>
    <div class="years-badge"><strong>15</strong><span>Years of Experience</span></div>
    <div class="about-copy">
      <div class="eyebrow">Why Choose Us</div>
      <h2 class="serif">Your Reliable Partner<br>in Escrow Accounting</h2>
      <p>For professionals in the title insurance industry, finding a trustworthy and budget-friendly solution for escrow accounting can be daunting. When choosing the right accounting partner, title companies and law firms need a group they can rely on, and that's where we come in. We bring years of hands-on experience, clear reporting and responsive support to every client we serve nationwide.</p>
      <span class="btn">About Us</span>
    </div>
  </div>
</section>

<section class="services">
  <div class="wrap">
    <span class="eyebrow">Our Services</span>
    <h2 class="serif">Our Escrow Accounting<br>Services</h2>
    <div class="service-grid">
      <article class="service-card">
        <svg width="38" height="38" viewBox="0 0 38 38"><rect x="4" y="6" width="22" height="28" fill="none" stroke="#c27c5e" stroke-width="2"/><line x1="9" y1="14" x2="21" y2="14" stroke="#c27c5e" stroke-width="2"/><line x1="9" y1="20" x2="21" y2="20" stroke="#c27c5e" stroke-width="2"/><circle cx="28" cy="26" r="7" fill="#c27c5e"/></svg>
        <h3 class="serif">Escrow Reconciliation Services</h3>
        <p>We complete monthly three-way reconciliations for every escrow account, identifying discrepancies early and keeping your records audit ready. Our detailed reports give you a clear view of balances, outstanding items and trends.</p>
        <span class="more">LEARN MORE →</span>
      </article>
      <article class="service-card">
        <svg width="38" height="38" viewBox="0 0 38 38"><rect x="5" y="4" width="24" height="30" fill="none" stroke="#c27c5e" stroke-width="2"/><path d="M11 19l5 5 9-10" fill="none" stroke="#c27c5e" stroke-width="2.5"/></svg>
        <h3 class="serif">Best Practices Certification</h3>
        <p>Prepare for best practices certification with confidence. We review your escrow procedures, document controls and policies, then help you close any gaps so your firm meets industry and underwriter expectations.</p>
        <span class="more">LEARN MORE →</span>
      </article>
      <article class="service-card">
        <svg width="38" height="38" viewBox="0 0 38 38"><circle cx="16" cy="16" r="10" fill="none" stroke="#c27c5e" stroke-width="2"/><line x1="23" y1="23" x2="33" y2="33" stroke="#c27c5e" stroke-width="3"/><rect x="12" y="12" width="8" height="8" fill="#c27c5e"/></svg>
        <h3 class="serif">Customized Review Services</h3>
        <p>Every firm has unique needs. Our customized reviews examine the areas that matter most to you, from disbursement testing to trust account audits, delivering practical findings and clear next steps for your team.</p>
        <span class="more">LEARN MORE →</span>
      </article>
    </div>
  </div>
</section>

<section class="contact">
  <div class="wrap">
    <div class="contact-info">
      <div class="eyebrow">Contact Us</div>
      <h2 class="serif">Get in touch !</h2>
      <p>Reach out to our team with any questions about escrow accounting. We respond quickly and are happy to discuss how we can support your firm.</p>
      <ul class="contact-list">
        <li><svg width="14" height="14" viewBox="0 0 14 14"><path d="M7 1a4 4 0 0 1 4 4c0 3-4 8-4 8S3 8 3 5a4 4 0 0 1 4-4z" fill="#c27c5e"/></svg>1210 Harbor View Road, Austin, TX 78701</li>
        <li><svg width="14" height="14" viewBox="0 0 14 14"><path d="M3 1l3 3-2 2a8 8 0 0 0 4 4l2-2 3 3-2 2C6 13 1 8 1 3z" fill="#c27c5e"/></svg>(555) 018-2044</li>
        <li><svg width="14" height="14" viewBox="0 0 14 14"><rect x="1" y="3" width="12" height="8" fill="none" stroke="#c27c5e" stroke-width="1.5"/><path d="M1 3l6 5 6-5" fill="none" stroke="#c27c5e" stroke-width="1.5"/></svg>hello@keystoneledger.com</li>
      </ul>
    </div>
    <form class="contact-form">
      <div class="form-row"><div class="field">First Name</div><div class="field">Last Name</div></div>
      <div class="form-row"><div class="field">Email</div><div class="field">Phone</div></div>
      <div class="form-row"><div class="field message">Message</div></div>
      <div class="form-actions"><span class="btn">Send</span><span class="consent"><i></i>I agree to the privacy policy</span></div>
    </form>
  </div>
</section>

<div class="map" role="img" aria-label="Street map showing the office location"></div>

<footer class="site-footer">
  <div class="wrap">
    <div class="footer-brand">
      <div class="brand"><span class="brand-mark"></span>KEYSTONE LEDGER</div>
      <p>Reliable, budget-friendly escrow accounting for title companies and law firms nationwide.</p>
      <div class="footer-social"><span class="dot-icon"></span><span class="dot-icon"></span></div>
    </div>
    <div class="footer-col">
      <h4>Navigation</h4>
      <ul><li>Home</li><li>About Us</li><li>Our Services</li><li>Contact Us</li></ul>
    </div>
    <div class="footer-col">
      <h4>Services</h4>
      <ul><li>Escrow Reconciliation Services</li><li>Best Practices Certification</li><li>Customized Review Services</li></ul>
    </div>
  </div>
</footer>
<div class="copyright">Copyright © Keystone Ledger Partners. All Rights Reserved.</div>

</body>
</html>
```